Tervolan Pty Ltd professional business card

A professional business card template using the colours from the supplied logo.
Clean crisp lines while, Modern while not being over the top.

Target Market(s)

Construction, commerical and industrial

Industry/Entity Type

Communications

Contact Information for Business Card

For a Communications, IT, Optical fibre installation company

Colors
37b8a4

```html
<!DOCTYPE html>
<html lang="en">
<head>
<meta charset="utf-8">
<title>Tervolan Business Card</title>
<link href="https://fonts.googleapis.com/css2?family=Montserrat:wght@400;500;600&display=swap" rel="stylesheet">
<style>
  :root {
    --canvas-bg: #e7e4df;
    --card-dark: #252525;
    --card-light: #ffffff;
    --teal: #1a94a2;
    --grey: #6d6e71;
    --ink: #3f4042;
  }
  * { margin: 0; padding: 0; box-sizing: border-box; }
  html, body {
    width: 1200px; height: 965px; overflow: hidden;
    background: var(--canvas-bg);
    font-family: "Montserrat", sans-serif;
  }
  .canvas { position: relative; width: 1200px; height: 965px; }
  .card {
    position: absolute; left: 276px; width: 648px; height: 370px;
    border-radius: 28px;
  }
  .card--front { top: 97px; background: var(--card-dark); }
  .card--back { top: 503px; background: var(--card-light); }

  .brand {
    position: absolute; display: flex; align-items: center;
    color: var(--grey); font-weight: 500; letter-spacing: 0.5px;
  }
  .brand__dot { border-radius: 50%; background: var(--teal); flex: none; }
  .card--front .brand { left: 0; right: 0; top: 150px; justify-content: center; font-size: 62px; gap: 16px; }
  .card--front .brand__dot { width: 22px; height: 22px; }
  .card--back .brand { left: 33px; top: 160px; font-size: 42px; gap: 10px; }
  .card--back .brand__dot { width: 15px; height: 15px; }

  .divider {
    position: absolute; left: 323px; top: 96px; width: 2px; height: 176px;
    background: var(--teal);
  }
  .contact { position: absolute; left: 346px; top: 90px; color: var(--ink); }
  .contact__name { color: var(--teal); font-weight: 600; font-size: 23px; letter-spacing: 0.6px; line-height: 1.1; }
  .contact__role { font-size: 14px; font-weight: 500; margin-top: 3px; }
  .contact__address { font-size: 16px; line-height: 23px; margin-top: 16px; color: var(--grey); }
  .contact__list { list-style: none; margin-top: 8px; }
  .contact__item { display: flex; align-items: center; gap: 10px; font-size: 17px; line-height: 24px; }
  .contact__item svg { width: 16px; height: 16px; fill: var(--ink); flex: none; }
</style>
</head>
<body>
<main class="canvas">
  <section class="card card--front">
    <div class="brand"><span class="brand__dot"></span><span>TERVOLAN</span></div>
  </section>

  <section class="card card--back">
    <div class="brand"><span class="brand__dot"></span><span>TERVOLAN</span></div>
    <div class="divider"></div>
    <div class="contact">
      <p class="contact__name">DANIEL OKAFOR</p>
      <p class="contact__role">Director</p>
      <p class="contact__address">Rua Nova Serra,<br>42, 2140-118 NJ</p>
      <ul class="contact__list">
        <li class="contact__item">
          <svg viewBox="0 0 24 24" aria-hidden="true"><path d="M6.6 10.8a15.1 15.1 0 0 0 6.6 6.6l2.2-2.2c.3-.3.7-.4 1-.2 1.1.4 2.3.6 3.6.6.6 0 1 .4 1 1V20c0 .6-.4 1-1 1A17 17 0 0 1 3 4c0-.6.4-1 1-1h3.5c.6 0 1 .4 1 1 0 1.3.2 2.5.6 3.6.1.3 0 .7-.2 1z"/></svg>
          <span>555-210-4836</span>
        </li>
        <li class="contact__item">
          <svg viewBox="0 0 24 24" aria-hidden="true"><path d="M2 5h20v14H2zm2 2v.4l8 5.2 8-5.2V7l-8 5.2z"/></svg>
          <span>daniel@tervolan.com</span>
        </li>
        <li class="contact__item">
          <svg viewBox="0 0 24 24" aria-hidden="true"><path d="M12 2a10 10 0 1 0 0 20 10 10 0 0 0 0-20zm-1 17.9A8 8 0 0 1 4.2 10L9 14.8v1c0 1.1.9 2 2 2zm6.9-2.5A2 2 0 0 0 16 16h-1v-3c0-.6-.4-1-1-1H8v-2h2c.6 0 1-.4 1-1V7h2a2 2 0 0 0 2-2v-.4a8 8 0 0 1 2.9 12.8z"/></svg>
          <span>www.tervolan.com</span>
        </li>
      </ul>
    </div>
  </section>
</main>
</body>
</html>
```